Business Card for a mobile physiotherapy company

I need a layout for a business card for a mobile physiotherapy company.
Slogan is "Mobile Physiotherapy - Your Road To Recovery"
Phone number is 867-402-5913
Email VantrePhysio@mailbright.ca (subject to change with website)
Website www.VantrePhysio.ca
My name and credentials: Kent Vantre Kent Vantre, BSc(kin), MPT, CAFCI, IMS
Information maybe included: Direct Billing, Services including Physiotherapy, IMS, acupuncture
Maybe include facebook and instagram logos
One side with the logo clean and sharp
Other side with details, try not to look too busy, keep everything concise

```html
<!DOCTYPE html>
<html lang="en">
<head>
<meta charset="utf-8">
<title>Vantre Therapy – Business Card</title>
<link href="https://fonts.googleapis.com/css2?family=Lato:wght@400;700&display=swap" rel="stylesheet">
<style>
  :root {
    --navy: #2c4a7a;
    --navy-deep: #243f6b;
    --green: #0f5a45;
    --paper: #ececec;
    --ink: #4a4f58;
    --stage: #2b2b2d;
    --white: #ffffff;
  }
  * { box-sizing: border-box; margin: 0; padding: 0; }
  html, body { width: 1200px; height: 800px; overflow: hidden; }
  body {
    background: var(--stage);
    font-family: "Lato", Arial, sans-serif;
    display: flex;
    align-items: center;
    justify-content: center;
    gap: 40px;
  }
  .card {
    width: 560px;
    height: 320px;
    position: relative;
    overflow: hidden;
  }

  /* Brand name placeholder: one colour, one weight, plain text */
  .brand {
    display: flex;
    align-items: center;
    gap: 10px;
    font-weight: 700;
    line-height: 1;
    white-space: nowrap;
  }
  .brand-mark {
    width: 14px;
    height: 14px;
    flex: none;
  }

  /* Front */
  .card-front {
    background: linear-gradient(160deg, var(--navy) 0%, var(--navy-deep) 100%);
    color: var(--white);
    display: flex;
    flex-direction: column;
    align-items: center;
    justify-content: center;
  }
  .card-front .brand { font-size: 40px; color: var(--white); }
  .card-front .brand-mark { width: 18px; height: 18px; background: var(--white); }
  .slogan {
    margin-top: 40px;
    font-size: 13.5px;
    letter-spacing: 0.3px;
    color: var(--white);
  }

  /* Back */
  .card-back { background: var(--paper); }
  .back-swoosh { position: absolute; inset: 0; }
  .back-brand {
    position: absolute;
    left: 22px;
    top: 96px;
    width: 230px;
    display: flex;
    justify-content: center;
  }
  .card-back .brand { font-size: 24px; color: var(--green); }
  .card-back .brand-mark { background: var(--green); }
  .divider {
    position: absolute;
    left: 262px;
    top: 46px;
    width: 1px;
    height: 152px;
    background: var(--ink);
    opacity: 0.7;
  }
  .details {
    position: absolute;
    left: 282px;
    top: 44px;
    color: var(--ink);
    font-size: 12px;
    line-height: 1.38;
  }
  .details .person { color: var(--navy); font-weight: 700; font-size: 15px; }
  .details .credentials { margin-bottom: 4px; }
  .services { list-style: none; margin-bottom: 4px; }
  .services li::before { content: "• "; }
  .contact { list-style: none; }
  .contact li { display: flex; align-items: center; gap: 6px; }
  .contact svg { width: 10px; height: 10px; flex: none; }
  .social {
    position: absolute;
    right: 20px;
    bottom: 9px;
    display: flex;
    align-items: center;
    gap: 5px;
    color: var(--white);
    font-size: 12px;
  }
  .social .dot { width: 12px; height: 12px; border-radius: 50%; background: var(--white); }
  .social .label { margin-right: 4px; }
</style>
</head>
<body>

  <section class="card card-front" aria-label="Card front">
    <div class="brand"><span class="brand-mark"></span>Vantre Therapy</div>
    <p class="slogan">Mobile Physiotherapy - Your Road To Recovery</p>
  </section>

  <section class="card card-back" aria-label="Card back">
    <svg class="back-swoosh" viewBox="0 0 560 320" preserveAspectRatio="none" aria-hidden="true">
      <path d="M0,198 C150,262 350,290 560,284 L560,320 L0,320 Z" fill="var(--navy)"/>
      <path d="M0,184 C160,250 370,275 530,278" fill="none" stroke="var(--green)" stroke-width="4"/>
    </svg>

    <div class="back-brand">
      <div class="brand"><span class="brand-mark"></span>Vantre Therapy</div>
    </div>

    <div class="divider"></div>

    <div class="details">
      <p class="person">Kent Vantre Kent Vantre</p>
      <p class="credentials">BSc (kin), MPT, CAFCI, IMS</p>
      <ul class="services">
        <li>Direct Billing</li>
        <li>Services including Physiotherapy</li>
        <li>IMS • Acupuncture</li>
      </ul>
      <ul class="contact">
        <li>
          <svg viewBox="0 0 10 10"><path d="M2,1 L4,3 L3,4 Q4,6 6,7 L7,6 L9,8 L8,9 Q4,9 1,5 Q1,2 2,1Z" fill="var(--ink)"/></svg>
          867-402-5913
        </li>
        <li>
          <svg viewBox="0 0 10 10"><rect x="0.5" y="2" width="9" height="6" fill="none" stroke="var(--ink)"/><path d="M0.5,2 L5,5.5 L9.5,2" fill="none" stroke="var(--ink)"/></svg>
          VantrePhysio@mailbright.ca
        </li>
        <li>
          <svg viewBox="0 0 10 10"><circle cx="5" cy="5" r="4.3" fill="none" stroke="var(--ink)"/><path d="M0.7,5 H9.3 M5,0.7 V9.3" stroke="var(--ink)" stroke-width="0.8"/><ellipse cx="5" cy="5" rx="2" ry="4.3" fill="none" stroke="var(--ink)" stroke-width="0.8"/></svg>
          www.VantrePhysio.ca
        </li>
      </ul>
    </div>

    <div class="social">
      <span class="label">Find us on</span>
      <span class="dot"></span>
      <span class="dot"></span>
    </div>
  </section>

</body>
</html>
```